Criminal Defense Law Firm needs Stationary design Theme for a Business Card, Envelope, and Letterhea

Our Law Firm is seeking a general design concept for a business card, letterhead, and Envelope.

Our website is QuillmoreAdvocates.com

A design for these three items is requested to keep branding in place for the firm. Would like to keep the Firm Colors on the website consistent with our branding on business cards, letterheads, and mailing envelopes #10 size to be exact.

We would like business cards printed front and back with Law firm Colors from website.

Letterhead with law firm colors as well. Design is not limited to just the header, but the footer can be utilized as well for email, website, phone, fax, etc.

Simple #10 envelope consisting of the same design principles set out in the previous two designs.

```html
<!DOCTYPE html>
<html lang="en">
<head>
<meta charset="utf-8">
<title>Quillmore Advocates — Letterhead &amp; Fax Cover</title>
<link rel="stylesheet" href="https://fonts.googleapis.com/css2?family=Spectral:wght@400&family=Arimo:wght@400;700&display=swap">
<style>
  :root {
    --backdrop: #ececec;
    --paper: #f7f7f6;
    --gold: #a8925f;
    --charcoal: #4a4a4a;
    --ink: #555555;
    --ink-soft: #6b6b6b;
    --rule: #8a8a8a;
    --tab-fill: #e2e2e2;
  }
  * { box-sizing: border-box; margin: 0; padding: 0; }
  html, body {
    width: 1200px; height: 815px; overflow: hidden;
    background: var(--backdrop);
  }
  .canvas { position: relative; width: 1200px; height: 815px; }

  .sheet {
    position: absolute; top: 72px;
    width: 482px; height: 682px;
    background: var(--paper);
  }
  .sheet--letterhead { left: 80px; }
  .sheet--fax { left: 638px; }
  .sheet__top-band { position: absolute; top: 0; left: 0; right: 0; height: 5px; background: var(--gold); }
  .sheet__bottom-band { position: absolute; bottom: 0; left: 0; right: 0; height: 10px; background: var(--charcoal); }

  .brand {
    position: absolute; top: 44px; left: 42px;
    display: flex; align-items: center; gap: 18px;
  }
  .brand__mark {
    width: 30px; height: 30px; border-radius: 50%;
    border: 1.5px solid var(--ink);
  }
  .brand__name {
    font-family: "Spectral", Georgia, serif;
    font-size: 14.5px; line-height: 15px; letter-spacing: 0.4px;
    color: var(--ink); text-transform: uppercase;
  }

  .fax-title {
    position: absolute; top: 33px; right: 38px;
    font-family: "Arimo", Arial, sans-serif;
    font-size: 66px; line-height: 66px; color: var(--ink);
  }

  .fax-details {
    position: absolute; top: 130px; left: 40px;
    width: 404px; border-collapse: collapse;
    font-family: "Arimo", Arial, sans-serif; font-size: 7.5px; font-weight: 700;
    color: var(--ink);
  }
  .fax-details td { border: 1px solid var(--rule); height: 14.7px; padding: 0 4px; }
  .fax-details .label { width: 43px; }
  .fax-details .value { width: 159px; }

  .fax-message {
    position: absolute; top: 218px; left: 40px;
    width: 404px; height: 386px;
    border: 1px solid var(--rule);
  }
  .fax-message__flags {
    display: flex; height: 14px; background: var(--tab-fill);
    border-bottom: 1px solid var(--rule);
    font-family: "Arimo", Arial, sans-serif; font-size: 7px; font-weight: 700;
    color: var(--ink);
  }
  .flag {
    display: flex; align-items: center; justify-content: center; gap: 3px;
    border-right: 1px solid var(--rule);
  }
  .flag:last-child { border-right: 0; }
  .flag__box { width: 5px; height: 5px; border: 0.8px solid var(--ink); }
  .fax-message__label {
    text-align: center; margin-top: 12px;
    font-family: "Arimo", Arial, sans-serif; font-size: 7.5px; color: var(--ink);
  }

  .contact-footer {
    position: absolute; left: 40px; right: 40px; bottom: 20px;
    display: flex; justify-content: space-between; align-items: baseline;
    font-family: "Arimo", Arial, sans-serif; font-size: 7px; color: var(--ink-soft);
  }
  .contact-footer__accent { color: var(--gold); }
  .contact-footer__web { letter-spacing: 1.6px; }
</style>
</head>
<body>
<main class="canvas">

  <section class="sheet sheet--letterhead" aria-label="Letterhead">
    <div class="sheet__top-band"></div>
    <div class="brand">
      <span class="brand__mark"></span>
      <p class="brand__name">Quillmore<br>Advocates</p>
    </div>
    <footer class="contact-footer">
      <span>2140 Larkspur Avenue, Fairview, NM 87000 · <span class="contact-footer__accent">Phone:</span> 555.014.2760</span>
      <span class="contact-footer__web">www.<span class="contact-footer__accent">quillmoreadvocates</span>.com</span>
    </footer>
    <div class="sheet__bottom-band"></div>
  </section>

  <section class="sheet sheet--fax" aria-label="Fax cover sheet">
    <div class="sheet__top-band"></div>
    <div class="brand">
      <span class="brand__mark"></span>
      <p class="brand__name">Quillmore<br>Advocates</p>
    </div>
    <h1 class="fax-title">FAX</h1>

    <table class="fax-details">
      <tr><td class="label">To:</td><td class="value"></td><td class="label">From:</td><td class="value"></td></tr>
      <tr><td class="label">Fax:</td><td class="value"></td><td class="label">Pages:</td><td class="value"></td></tr>
      <tr><td class="label">Phone:</td><td class="value"></td><td class="label">Date:</td><td class="value"></td></tr>
      <tr><td class="label">Re:</td><td class="value"></td><td class="label">CC:</td><td class="value"></td></tr>
    </table>

    <div class="fax-message">
      <div class="fax-message__flags">
        <span class="flag" style="width:80px"><span class="flag__box"></span>Urgent</span>
        <span class="flag" style="width:78px"><span class="flag__box"></span>For Review</span>
        <span class="flag" style="width:90px"><span class="flag__box"></span>Please Comment</span>
        <span class="flag" style="width:78px"><span class="flag__box"></span>Please Reply</span>
        <span class="flag" style="width:78px"><span class="flag__box"></span>Please Recycle</span>
      </div>
      <p class="fax-message__label">COMMENTS:</p>
    </div>

    <footer class="contact-footer">
      <span>2140 Larkspur Avenue, Fairview, NM 87000 · <span class="contact-footer__accent">Phone:</span> 555.014.2760</span>
      <span class="contact-footer__web">www.<span class="contact-footer__accent">quillmoreadvocates</span>.com</span>
    </footer>
    <div class="sheet__bottom-band"></div>
  </section>

</main>
</body>
</html>
```